Poster for pawn shop lobby

Looking for green and gold as my colors, like the picture shown of my old poster. This time I'm contemplating with doing pictures as well as just text. Here are ideas of things I buy and give loans on. We want to emphasize jewelry, laptops, game systems, tools. I'm open-minded.
Old & Broken Gold
Jewelry & Collectibles
Diamonds
Video Games & Systems
Up-to-date Computers & Laptops
Tablets
Cameras
Power Tools
Home & Garden Equipment
Sports Equipment
Watches
Antique Collectibles
Musical Instruments
And anything else of value

```html
<!DOCTYPE html>
<html lang="en">
<head>
<meta charset="UTF-8">
<title>We Buy and Give Loans On</title>
<link href="https://fonts.googleapis.com/css2?family=Bebas+Neue&family=Arimo:wght@700&display=swap" rel="stylesheet">
<style>
  :root {
    --gold-light: #e3cc93;
    --gold-mid: #c9ab62;
    --gold-dark: #a88a44;
    --headline-ink: #333333;
    --green-top: #2fbd00;
    --green-bottom: #1b7a00;
    --item-tone-light: #2f8f14;
    --item-tone-dark: #0f3d06;
    --white: #ffffff;
  }
  * { margin: 0; padding: 0; box-sizing: border-box; }
  html, body { width: 1200px; height: 960px; overflow: hidden; }
  body { font-family: "Arimo", Arial, sans-serif; }
  .poster {
    position: relative;
    width: 1200px;
    height: 960px;
    overflow: hidden;
    background: linear-gradient(180deg, var(--green-top) 0%, var(--green-bottom) 100%);
  }
  .gold-band {
    position: absolute;
    left: 0; top: 0;
    width: 1200px; height: 248px;
    background:
      repeating-linear-gradient(0deg, rgba(255,255,255,0.06) 0 1px, rgba(0,0,0,0.04) 1px 3px),
      linear-gradient(100deg, var(--gold-dark) 0%, var(--gold-light) 30%, var(--gold-mid) 55%, var(--gold-light) 75%, var(--gold-dark) 100%);
  }
  .headline {
    position: absolute;
    left: 0; top: 72px;
    width: 1200px;
    text-align: center;
    font-family: "Bebas Neue", Impact, sans-serif;
    font-weight: 400;
    font-size: 128px;
    line-height: 128px;
    color: var(--headline-ink);
    -webkit-text-stroke: 3px var(--headline-ink);
    letter-spacing: -2.5px;
    white-space: nowrap;
  }
  .item-visual {
    position: absolute;
    background: radial-gradient(ellipse at center, var(--item-tone-light) 0%, var(--item-tone-dark) 100%);
    border-radius: 6px;
  }
  .item-label {
    position: absolute;
    top: 524px;
    font-size: 29px;
    line-height: 34px;
    font-weight: 700;
    color: var(--white);
    text-align: center;
    white-space: nowrap;
  }
  .visual-jewelry { left: 80px; top: 390px; width: 255px; height: 120px; border-radius: 50% 50% 12px 12px; }
  .visual-laptop { left: 352px; top: 362px; width: 248px; height: 148px; }
  .visual-games { left: 652px; top: 395px; width: 243px; height: 85px; }
  .visual-tools { left: 960px; top: 340px; width: 195px; height: 170px; }
  .label-jewelry { left: 80px; width: 255px; }
  .label-laptops { left: 356px; width: 250px; }
  .label-games { left: 640px; width: 265px; }
  .label-tools { left: 960px; width: 195px; top: 529px; }
  .item-list {
    position: absolute;
    left: 0; top: 685px;
    width: 1200px;
    font-size: 35.5px;
    font-weight: 700;
    line-height: 44px;
    color: var(--white);
    text-align: center;
  }
  .item-list .line { display: block; white-space: nowrap; }
</style>
</head>
<body>
<main class="poster">
  <header class="gold-band">
    <h1 class="headline">WE BUY AND GIVE LOANS ON</h1>
  </header>

  <div class="item-visual visual-jewelry" role="img" aria-label="Pile of gold jewelry, rings and chains, tinted green"></div>
  <div class="item-visual visual-laptop" role="img" aria-label="Open laptop computer, tinted green"></div>
  <div class="item-visual visual-games" role="img" aria-label="Row of video game consoles and handhelds, tinted green"></div>
  <div class="item-visual visual-tools" role="img" aria-label="Hand tools: screwdrivers, pliers and hammer, tinted green"></div>

  <p class="item-label label-jewelry">JEWELRY</p>
  <p class="item-label label-laptops">LAPTOPS</p>
  <p class="item-label label-games">GAME SYSTEMS</p>
  <p class="item-label label-tools">TOOLS</p>

  <p class="item-list">
    <span class="line">Old &amp; Broken Gold / Jewelry &amp; Collectibles / Diamonds / Video</span>
    <span class="line">Games &amp; Systems / Up-to-date Computers &amp; Laptops / Tablets</span>
    <span class="line">/ Cameras / Power Tools / Home &amp; Garden Equipment / Sports</span>
    <span class="line">Equipment / Watches / Antique Collectibles &nbsp;/ Musical Instru-</span>
    <span class="line">ments / And anything else of value</span>
  </p>
</main>
</body>
</html>
```